Wordpress Design Project

I have a main site www.smilesprouthub.example for 9 dental offices. I want a designed wordpress mini-site template that I can use to create mini sites for each location and related projects that keeps the look and feel of the home site.
Updates

I'm getting different designs from my original web site. Maybe I'm confusing the designers but to clarify:

what I want is to keep the same graphics as we already have on this site www.smilesprouthub.example and just convert it to a Wordpress site template to be used as individual MINI sites. 

No new designs needed, same design just different platform.

Target Market(s)

see site www.smilesprouthub.example

Industry/Entity Type

Dental

Requirements
Must have
• Can we make the Logo larger?
Should not have
• I think you're basing your designs on smilesprouthubwestvale.example but I specifically said it should be based on the home site which is www.smilesprouthub.example
Please view the difference. I need for it to have the same APPEARANCE. Please!
http://www.smilesprouthub.example/

```html
<!DOCTYPE html>
<html lang="en">
<head>
<meta charset="utf-8">
<title>Smile Sprout Hub – Kids Dental Care</title>
<link href="https://fonts.googleapis.com/css2?family=Encode+Sans+Condensed:wght@300;400&family=PT+Sans:ital,wght@0,400;0,700;1,400&display=swap" rel="stylesheet">
<style>
:root{
  --purple:#7a33d4;
  --purple-dark:#6526bf;
  --purple-light:#9a63e6;
  --ink:#222;
  --text:#444;
  --muted:#666;
  --rule:#dcdcdc;
  --footer:#f2f2f2;
  --bar:#e6e6e6;
  --dark-btn:#333;
}
*{box-sizing:border-box;margin:0;padding:0}
html,body{width:830px;height:1200px;overflow:hidden;background:#fff}
body{font-family:"PT Sans",sans-serif;color:var(--text)}
.page{position:relative;width:830px;height:1200px;overflow:hidden}
.abs{position:absolute}
ul{list-style:none}

.top-line{left:0;top:0;width:830px;height:5px;background:#d5d5d5}
.brand{left:26px;top:48px;display:flex;align-items:center;gap:7px;font-size:15px;font-weight:700;color:var(--purple)}
.brand-dot{width:14px;height:14px;border-radius:50%;background:var(--purple)}
.phone{right:24px;top:33px;font-size:15px;color:var(--ink);display:flex;align-items:center;gap:6px}
.email{right:22px;top:59px;font-size:10px;color:var(--ink);display:flex;align-items:center;gap:6px}
.social{display:flex;gap:6px}
.social span{width:18px;height:18px;border-radius:50%;background:var(--purple)}
.header-social{right:24px;top:85px}

.nav{left:0;top:120px;width:830px;height:44px;background:linear-gradient(var(--purple-light),var(--purple) 45%,var(--purple-dark))}
.nav ul{display:flex;height:44px;padding-left:19px}
.nav li{font-family:"Encode Sans Condensed",sans-serif;font-weight:300;font-size:12px;color:#fff;line-height:44px;text-transform:uppercase}
.nav li.active{background:rgba(255,255,255,.18);width:75px;text-align:center}
.nav li + li{margin-left:0}

.hero-photo{left:0;top:164px;width:559px;height:298px;background:linear-gradient(120deg,#d9cfc4,#efe6dc 45%,#c9b7a6)}
.hero-copy{left:587px;top:198px;width:230px}
.hero-copy .welcome{font-family:"Encode Sans Condensed",sans-serif;font-size:16px;color:var(--ink)}
.hero-copy h1{font-family:"Encode Sans Condensed",sans-serif;font-weight:300;font-size:24px;color:var(--purple);line-height:1.1;margin-top:1px}
.hero-copy .lead{font-size:9.7px;color:var(--ink);line-height:14.5px;margin-top:6px}
.hero-copy .sub{font-size:8.6px;color:var(--muted);line-height:14.5px;margin-top:4px}
.checks{margin-top:10px}
.checks li{font-size:8.8px;font-style:italic;color:var(--text);display:flex;align-items:center;gap:6px;height:18.6px}
.btn{display:inline-block;font-family:"Encode Sans Condensed",sans-serif;font-size:11px;color:#fff;text-align:center;text-transform:uppercase}
.btn-direction{left:589px;top:398px;width:91px;height:24px;line-height:24px;background:var(--purple)}
.btn-more{left:686px;top:398px;width:88px;height:24px;line-height:24px;background:var(--dark-btn)}
.hero-rule{left:0;top:462px;width:830px;height:1px;background:var(--rule)}

.intro-title{left:23px;top:483px;font-size:14.5px;color:var(--ink)}
.intro-photo{left:21px;top:511px;width:123px;height:131px;background:linear-gradient(135deg,#8fc4e4,#f0cdbd 55%,#d99e8c)}
.intro-text{left:157px;top:510px;width:330px;font-size:9.2px;line-height:15.4px;color:var(--text)}
.intro-text p + p{margin-top:6px}
.read-more{left:157px;top:633px;font-size:9.5px;font-weight:700;color:var(--ink)}
.content-rule{left:23px;top:693px;width:487px;height:1px;background:var(--rule)}
.content-divider{left:510px;top:490px;width:1px;height:413px;background:var(--rule)}

.loc-title{left:24px;top:710px;font-size:14px;color:var(--ink)}
.location{font-size:8.8px;line-height:17px;color:var(--text)}
.location strong{color:var(--ink);font-size:9.2px}

.card-photo{border:4px solid #fff;box-shadow:0 0 3px rgba(0,0,0,.3)}
.card-title{font-size:14px;color:var(--ink)}
.card-text{font-size:8.6px;line-height:14.6px;color:var(--muted);width:165px}
.card-btn{font-size:10px;color:#fff;background:var(--purple);text-align:center;height:20px;line-height:20px}

.footer{left:0;top:940px;width:830px;height:218px;background:var(--footer);border-top:1px solid #e4e4e4}
.foot-head{font-size:12px;color:var(--purple)}
.quick{font-size:9.3px;color:var(--ink)}
.quick li{height:22px;display:flex;align-items:center;gap:7px}
.quick li::before{content:"";border-left:3px solid #555;border-top:2.5px solid transparent;border-bottom:2.5px solid transparent}
.foot-rule{width:1px;height:134px;top:992px;background:#d5d5d5}
.contact-info{left:443px;top:990px;font-size:9.5px;line-height:19.5px;color:var(--ink)}
.connect-links{left:633px;top:1024px;font-size:9.5px;font-style:italic;color:var(--ink)}
.bottom-bar{left:0;top:1158px;width:830px;height:42px;background:var(--bar);font-size:8.8px;color:var(--muted)}
.bottom-bar .copy{position:absolute;left:37px;top:13px}
.bottom-bar .legal{position:absolute;right:28px;top:13px}
</style>
</head>
<body>
<div class="page">
  <div class="abs top-line"></div>

  <header>
    <div class="abs brand"><span class="brand-dot"></span>Smile Sprout Hub</div>
    <div class="abs phone">
      <svg width="9" height="14" viewBox="0 0 9 14"><path d="M2 1h3l1 3-2 1.5c.6 1.6 1.4 2.8 2.6 3.8L8 8l1 3-1.6 2C3.5 12 .6 7.5 1 2z" fill="#222"/></svg>
      555 014 2760
    </div>
    <div class="abs email">
      <svg width="15" height="10" viewBox="0 0 15 10"><rect width="15" height="10" fill="#222"/><path d="M0 0l7.5 6L15 0" fill="none" stroke="#fff" stroke-width="1.2"/></svg>
      westvale@smilesprouthub.example
    </div>
    <div class="abs social header-social" aria-label="Social links"><span></span><span></span><span></span><span></span></div>
  </header>

  <nav class="abs nav">
    <ul>
      <li class="active">Home</li>
      <li style="margin-left:17px">Appointment</li>
      <li style="margin-left:37px">Gallery</li>
      <li style="margin-left:37px">Services</li>
      <li style="margin-left:36px">About Us</li>
      <li style="margin-left:37px">Promise</li>
      <li style="margin-left:37px">Blog</li>
      <li style="margin-left:37px">Log In</li>
      <li style="margin-left:37px">FAQ</li>
      <li style="margin-left:37px">Contact</li>
    </ul>
  </nav>

  <section class="hero">
    <div class="abs hero-photo" role="img" aria-label="Photo of a mother and young son brushing teeth together"></div>
    <div class="abs hero-copy">
      <p class="welcome">WELCOME TO OUR SITE!</p>
      <h1>KIDS DENTAL CARE</h1>
      <p class="lead">Lorem ipsum dolor sit amet, consectetuer adipiscing elit. Nam cursus.</p>
      <p class="sub">Morbi ut mi. Nullam enim leo, egestas id, condimentum at, laoreet mattis, massa.</p>
      <ul class="checks">
        <li><svg width="12" height="10" viewBox="0 0 12 10"><path d="M1 5l3.5 3.5L11 1" fill="none" stroke="#222" stroke-width="2"/></svg>Praesent mauris ante, elementum et.</li>
        <li><svg width="12" height="10" viewBox="0 0 12 10"><path d="M1 5l3.5 3.5L11 1" fill="none" stroke="#222" stroke-width="2"/></svg>Bibendum at, posuere sit amet, nibh.</li>
        <li><svg width="12" height="10" viewBox="0 0 12 10"><path d="M1 5l3.5 3.5L11 1" fill="none" stroke="#222" stroke-width="2"/></svg>Duis tincidunt lectus quis dui viverra vestibulum.</li>
      </ul>
    </div>
    <span class="abs btn btn-direction">Get Direction</span>
    <span class="abs btn btn-more">Learn More</span>
    <div class="abs hero-rule"></div>
  </section>

  <main>
    <h2 class="abs intro-title" style="font-weight:400">Look and Click Below for the Office to Serve you.</h2>
    <div class="abs intro-photo" role="img" aria-label="Photo of a child at a dental check-up"></div>
    <div class="abs intro-text">
      <p>Smile Sprout Hub accepts all private insurances, StateDent &amp; all major credit cards, Financial assistance may be arranged for those with financial need. At Smile Sprout Hub, we are your servants providing the highest quality dental care to you and your loved ones.</p>
      <p>Lorem ipsum dolor sit amet, consectetuer adipiscing elit. Nam cursus. Morbi ut mi. Nullam enim leo, egestas id, condimentum at, laoreet mattis, massa. Sed eleifend nonummy diam.</p>
    </div>
    <span class="abs read-more">READ MORE</span>
    <div class="abs content-rule"></div>
    <div class="abs content-divider"></div>

    <h2 class="abs loc-title" style="font-weight:400">Our Location</h2>
    <div class="abs location" style="left:27px;top:740px"><strong>Maple Crest</strong><br>2210 Maple Crest Rd<br>Westvale, CA 90990<br>(555) 014-1101</div>
    <div class="abs location" style="left:151px;top:740px"><strong>Harbor East</strong><br>4410 Harbor Line Ave<br>Westvale, CA 90991<br>(555) 014-1102</div>
    <div class="abs location" style="left:270px;top:738px"><strong>Pine Ridge</strong><br>8820 E. Orchard Way<br>Pine Ridge, CA 90992<br>(555) 014-1103</div>
    <div class="abs location" style="left:392px;top:738px"><strong>Linden Park</strong><br>1775 E. Linden Ave<br>Westvale, CA 90993<br>(555) 014-1104</div>
    <div class="abs location" style="left:27px;top:833px"><strong>Brookhaven</strong><br>6630 Sunfield Blvd<br>Brookhaven, CA 90994<br>(555) 014-1105</div>
    <div class="abs location" style="left:151px;top:833px"><strong>Fairmont</strong><br>1940 E. Willow St<br>Fairmont, CA 90995<br>(555) 014-1106</div>
    <div class="abs location" style="left:270px;top:832px"><strong>Westvale</strong><br>3300 W. Cedar Ave. Suite<br>Westvale, CA 90996<br>(555) 014-1107</div>
    <div class="abs location" style="left:392px;top:832px"><strong>Lakeport</strong><br>9050 Bayshore Blvd<br>Lakeport, CA 90997<br>(555) 014-1108</div>

    <aside>
      <div class="abs card-photo" style="left:529px;top:490px;width:112px;height:108px;background:linear-gradient(135deg,#c7dbe8,#f3f3f3 50%,#d8c2b2)" role="img" aria-label="Photo of a dentist examining a boy"></div>
      <h3 class="abs card-title" style="left:654px;top:488px;font-weight:400">Dental Services</h3>
      <p class="abs card-text" style="left:655px;top:509px">Lorem ipsum dolor sit amet, consectetuer adipiscing elit. Nam cursus. Morbi ut mi. Nullam enim leo, egestas id, condimentum at</p>
      <span class="abs card-btn" style="left:656px;top:575px;width:64px">learn more</span>

      <div class="abs card-photo" style="left:529px;top:635px;width:112px;height:108px;background:linear-gradient(135deg,#bcd6e6,#efe3dc 55%,#c9a596)" role="img" aria-label="Photo of a girl smiling in a dental chair"></div>
      <h3 class="abs card-title" style="left:654px;top:633px;font-weight:400">About Our Clinic</h3>
      <p class="abs card-text" style="left:655px;top:654px">Lorem ipsum dolor sit amet, consectetuer adipiscing elit. Nam cursus. Morbi ut mi. Nullam enim leo, egestas id, condimentum at</p>
      <span class="abs card-btn" style="left:656px;top:720px;width:64px">learn more</span>

      <div class="abs card-photo" style="left:532px;top:779px;width:114px;height:108px;background:linear-gradient(160deg,#f6f1e4,#e9d39a 60%,#d4b25a)" role="img" aria-label="Photo of a smiling girl giving two thumbs up"></div>
      <h3 class="abs card-title" style="left:658px;top:777px;font-weight:400">Make Appointment</h3>
      <p class="abs card-text" style="left:659px;top:798px">Lorem ipsum dolor sit amet, consectetuer adipiscing elit. Nam cursus. Morbi ut mi. Nullam enim leo, egestas id, condimentum at</p>
      <span class="abs card-btn" style="left:659px;top:865px;width:69px">CLICK HERE</span>
    </aside>
  </main>

  <footer>
    <div class="abs footer"></div>
    <h4 class="abs foot-head" style="left:38px;top:961px;font-weight:400">Quick Links</h4>
    <ul class="abs quick" style="left:40px;top:985px"><li>Home</li><li>Appointment</li><li>Promise</li><li>Gallery</li><li>Services</li><li>About Us</li></ul>
    <ul class="abs quick" style="left:172px;top:985px"><li>Contact</li><li>FAQ's</li><li>Patient Log In</li><li>Locations</li><li>Blog</li></ul>
    <ul class="abs quick" style="left:304px;top:985px"><li>Our Services</li><li>Sub Menus 1</li><li>Sub Menus 2</li><li>Sub Menus 3</li><li>Sub Menus 4</li></ul>
    <div class="abs foot-rule" style="left:409px"></div>
    <h4 class="abs foot-head" style="left:443px;top:961px;font-weight:400">Contact Info</h4>
    <div class="abs contact-info">Smile Sprout Hub Westvale<br>3300 West Cedar Ave.<br>Westvale, CA 90996<br>Call us 555-014-2250</div>
    <div class="abs foot-rule" style="left:598px"></div>
    <h4 class="abs foot-head" style="left:630px;top:961px;font-weight:400">Get Connected</h4>
    <div class="abs social" style="left:632px;top:992px"><span></span><span></span><span></span><span></span></div>
    <p class="abs connect-links">Friends | Updates | Feed | Network</p>
    <div class="abs bottom-bar">
      <span class="copy">Copyright © 2012 Company Name &nbsp;|&nbsp; All right reserved</span>
      <span class="legal">Term &amp; Conditions &nbsp;|&nbsp; Privacy Policy</span>
    </div>
  </footer>
</div>
</body>
</html>
```